Thankyou Card

- Thank you cards for my buyers
We are an online women's fashion boutique, we are after a thank you card that will be distributed after purchase
ideally on the card it will have logo - Website - Slogan- A thank you message
The card will be Bright, Fun & Inviting wanting the customer to return to our site
Attached it a copy of our logo web page and slogan -

Website - zelvora.com.au

Industry/Entity Type

Fashion

Requirements
Must have
• Business Name - Zelvora
Web Address - www.zelvora.com.au
Thank you for your purchase note
Slogan - Live, Laugh, Love & Shop...

```html
<!DOCTYPE html>
<html lang="en">
<head>
<meta charset="utf-8">
<title>Zelvora – Thank You Card</title>
<link rel="stylesheet" href="https://fonts.googleapis.com/css2?family=Tinos&family=Yesteryear&family=Petit+Formal+Script&display=swap">
<style>
  :root {
    --backdrop: #ececec;
    --card: #fdfdfd;
    --ink: #1a1a1a;
    --brand-red: #c8143c;
    --ornament-grey: #e3e3e3;
    --card-shadow: rgba(0, 0, 0, 0.12);
  }
  * { box-sizing: border-box; margin: 0; padding: 0; }
  html, body {
    width: 1200px;
    height: 982px;
    overflow: hidden;
    background: var(--backdrop);
  }
  .canvas {
    width: 1200px;
    height: 982px;
    display: flex;
    flex-direction: column;
    align-items: center;
    justify-content: center;
    gap: 50px;
  }
  .card {
    position: relative;
    width: 740px;
    height: 423px;
    background: var(--card);
    box-shadow: 0 6px 18px var(--card-shadow);
    overflow: hidden;
  }

  /* Back side: thank-you message */
  .card-back .ornament {
    position: absolute;
    left: 50%;
    top: 50%;
    width: 300px;
    height: 260px;
    transform: translate(-50%, -50%);
    border-radius: 50%;
    background: radial-gradient(ellipse at center, var(--ornament-grey) 0%, rgba(227,227,227,0.55) 60%, rgba(227,227,227,0) 100%);
  }
  .card-back .thanks {
    position: absolute;
    left: 0;
    right: 0;
    top: 50%;
    transform: translateY(-50%);
    text-align: center;
    font-family: "Yesteryear", cursive;
    font-size: 46px;
    color: var(--brand-red);
    letter-spacing: 1px;
  }
  .card-back .brand-name {
    position: absolute;
    left: 30px;
    bottom: 28px;
    font-family: "Tinos", serif;
    font-weight: 400;
    font-size: 20px;
    line-height: 1;
    color: var(--ink);
  }
  .card-back .web {
    position: absolute;
    right: 30px;
    bottom: 28px;
    font-family: "Tinos", serif;
    font-weight: 400;
    font-size: 15px;
    line-height: 1;
    color: var(--ink);
    letter-spacing: 0.5px;
  }

  /* Front side: brand name, slogan, web band */
  .card-front .brand-name {
    position: absolute;
    left: 60px;
    top: 100px;
    font-family: "Tinos", serif;
    font-weight: 400;
    font-size: 96px;
    line-height: 1;
    color: var(--ink);
  }
  .card-front .slogan {
    position: absolute;
    right: 70px;
    top: 222px;
    font-family: "Petit Formal Script", cursive;
    font-size: 24px;
    color: var(--ink);
  }
  .card-front .web-band {
    position: absolute;
    left: 0;
    right: 0;
    top: 300px;
    height: 40px;
    background: var(--brand-red);
    display: flex;
    align-items: center;
    justify-content: center;
  }
  .card-front .web-band .web {
    font-family: "Tinos", serif;
    font-weight: 400;
    font-size: 17px;
    color: #ffffff;
    letter-spacing: 0.5px;
  }
</style>
</head>
<body>
  <main class="canvas">
    <section class="card card-back">
      <div class="ornament" role="img" aria-label="Symmetrical pale grey swirl ornament behind the thank-you message"></div>
      <p class="thanks">Thank you for your purchase</p>
      <p class="brand-name">Zelvora</p>
      <p class="web">www.zelvora.com.au</p>
    </section>

    <section class="card card-front">
      <p class="brand-name">Zelvora</p>
      <p class="slogan">Live, Laugh, Love &amp; Shop...</p>
      <div class="web-band">
        <span class="web">www.zelvora.com.au</span>
      </div>
    </section>
  </main>
</body>
</html>
```